Offshore Energy Projects Management Consultancy needs a business card design

Logo available. We provide teams to deliver engineering consultancy, project management and delivery teams mainly in the offshore renewables sector. The company is all about bringing the right people to a project to deliver the scope.

The business card will be used for all staff.

The business card should be quite simple, vibrant and uncluttered but convey experience, enthusiasm and integration.

Target Market(s)

Energy Project Developers and Tier 1 construction companies

Contact Information for Business Card

Logo should be on the back of the card. I'm happy for the designer to play with the colour of the logo and background colour.

Front of the card should convey all the must have information in a clear and professional manner but without being overly traditional.

Colors

Designer to choose colors to be used in the design.

Requirements
Must have
• Land Line Tel Number, Mobile Tel Number, Email, business address, web address.

```html
<!DOCTYPE html>
<html lang="en">
<head>
<meta charset="utf-8">
<title>Tidewater Projects Group – Business Card</title>
<link href="https://fonts.googleapis.com/css2?family=Rubik:wght@400;500&display=swap" rel="stylesheet">
<style>
  :root {
    --stage: #1d1d1e;
    --card: #1a1a1b;
    --card-edge: #262627;
    --blue: #2a8fdc;
    --blue-light: #3aa9ea;
    --white: #f4f4f4;
    --grey: #8a8a8a;
  }
  * { margin: 0; padding: 0; box-sizing: border-box; }
  html, body {
    width: 1200px; height: 1200px; overflow: hidden;
    background: var(--stage);
    font-family: "Rubik", sans-serif;
  }
  .canvas { position: relative; width: 1200px; height: 1200px; }
  .card {
    position: absolute; left: 150px;
    width: 900px; height: 514px;
    background: var(--card);
    border: 1px solid var(--card-edge);
    border-radius: 22px;
    box-shadow: 0 20px 40px rgba(0,0,0,.5);
  }
  .card--back { top: 60px; display: flex; align-items: center; justify-content: center; }
  .card--front { top: 626px; }

  .brand { display: flex; align-items: center; gap: 18px; }
  .brand__dot { width: 34px; height: 34px; border-radius: 50%; background: var(--blue); }
  .brand__name {
    font-weight: 500; font-size: 38px; letter-spacing: 1px;
    color: var(--blue-light); text-transform: uppercase; line-height: 1.1;
  }
  .card--front .brand { position: absolute; left: 70px; top: 220px; }
  .card--front .brand__name { font-size: 30px; }

  .divider {
    position: absolute; left: 470px; top: 110px;
    width: 2px; height: 300px; background: var(--blue);
  }
  .contact { position: absolute; left: 510px; top: 118px; color: var(--white); }
  .contact__name { font-weight: 500; font-size: 30px; letter-spacing: 1px; }
  .contact__role { font-size: 21px; color: var(--blue-light); letter-spacing: 1px; margin-top: 2px; }
  .contact__list { list-style: none; margin-top: 24px; }
  .contact__item {
    display: flex; align-items: center; gap: 14px;
    font-size: 20px; letter-spacing: 1px; line-height: 31px;
  }
  .contact__item svg { width: 18px; height: 18px; fill: var(--blue); flex: none; }
  .contact__address { margin-top: 18px; font-size: 20px; letter-spacing: 1px; line-height: 28px; }
</style>
</head>
<body>
<div class="canvas">

  <section class="card card--back" aria-label="Card back">
    <div class="brand">
      <span class="brand__dot"></span>
      <span class="brand__name">Tidewater Projects Group</span>
    </div>
  </section>

  <section class="card card--front" aria-label="Card front">
    <div class="brand">
      <span class="brand__dot"></span>
      <span class="brand__name">Tidewater<br>Projects Group</span>
    </div>

    <div class="divider"></div>

    <div class="contact">
      <div class="contact__name">Marcus Ellery</div>
      <div class="contact__role">CEO/Founder</div>
      <ul class="contact__list">
        <li class="contact__item">
          <svg viewBox="0 0 24 24"><path d="M6.6 10.8a15 15 0 0 0 6.6 6.6l2.2-2.2c.3-.3.7-.4 1-.2 1.1.4 2.3.6 3.6.6.6 0 1 .4 1 1V20c0 .6-.4 1-1 1A17 17 0 0 1 3 4c0-.6.4-1 1-1h3.5c.6 0 1 .4 1 1 0 1.3.2 2.5.6 3.6.1.3 0 .7-.2 1z"/></svg>
          555-014-3872
        </li>
        <li class="contact__item">
          <svg viewBox="0 0 24 24"><path d="M7 3h10v4H7zM4 8h16a2 2 0 0 1 2 2v6h-4v5H6v-5H2v-6a2 2 0 0 1 2-2zm4 8v3h8v-3z"/></svg>
          555-014-3872
        </li>
        <li class="contact__item">
          <svg viewBox="0 0 24 24"><path d="M2 5h20v14H2zm2 2v.5l8 5 8-5V7l-8 5z"/></svg>
          marcus@tidewatergroup.example
        </li>
        <li class="contact__item">
          <svg viewBox="0 0 24 24"><path d="M12 2a10 10 0 1 0 0 20 10 10 0 0 0 0-20zm6.9 9h-3a15 15 0 0 0-1.3-6A8 8 0 0 1 18.9 11zM12 4c.9 1.3 1.7 3.8 1.9 7h-3.8C10.3 7.8 11.1 5.3 12 4zM9.4 5a15 15 0 0 0-1.3 6h-3A8 8 0 0 1 9.4 5zM5.1 13h3a15 15 0 0 0 1.3 6 8 8 0 0 1-4.3-6zM12 20c-.9-1.3-1.7-3.8-1.9-7h3.8c-.2 3.2-1 5.7-1.9 7zm2.6-1a15 15 0 0 0 1.3-6h3a8 8 0 0 1-4.3 6z"/></svg>
          www.tidewatergroup.example
        </li>
      </ul>
      <div class="contact__address">
        118 Harbour Street<br>
        Suite 210, Port Calder<br>
        NS 40217
      </div>
    </div>
  </section>

</div>
</body>
</html>
```